New website design

Hello again, we need you to create a basic, standard website with a homepage, 'contact us' page with reply form, 'pricing page' and 'about us' page. We would like to see most design elements carried over from www.tallowpine.com, our primary website. You can also use the front page of the attached brochure as inspiration for the homepage. The second attachment shows the pricing page (image on the right) with vertical columns - that's a good template for you to use on the pricing page for the website. The third attachment contains the text for the pricing page...just don't use that layout, try and duplicate the vertical layout example.
Target Market(s)
hospitals/medical care facilities
Coding
Coded - Design and coding required
Number of Pages Required
4 page
Look and feel

```html
<!DOCTYPE html>
<html lang="en">
<head>
<meta charset="utf-8">
<title>TallowPine — Packaging &amp; Sterilization</title>
<link href="https://fonts.googleapis.com/css2?family=Poppins:wght@400;500;600&display=swap" rel="stylesheet">
<style>
:root{
  --blue:#1479a7;
  --blue-deep:#0f6a94;
  --ink:#2b2f36;
  --slate:#343b43;
  --white:#ffffff;
  --muted:#8a9098;
  --line:#dcdfe3;
}
*{box-sizing:border-box;margin:0;padding:0}
html,body{width:1200px;height:3578px;overflow:hidden;background:var(--white)}
body{font-family:"Poppins",sans-serif;color:var(--ink)}
.page{position:relative;width:1200px;height:3578px;overflow:hidden}
.backdrop{position:absolute;left:0;top:0}
.abs{position:absolute}

/* header */
.site-header{position:absolute;left:0;top:0;width:1200px;height:72px;background:var(--white);z-index:3}
.brand{position:absolute;left:88px;top:14px;display:flex;align-items:center;gap:10px;font-size:32px;font-weight:400;color:var(--ink)}
.brand-dot{width:34px;height:34px;border-radius:50%;background:var(--blue)}
.main-nav{position:absolute;left:601px;top:30px;display:flex;gap:33px;font-size:15px;font-weight:500}
.main-nav a{color:var(--ink);text-decoration:none}
.main-nav a.active{color:var(--blue);border-bottom:1px solid var(--blue);padding-bottom:2px}
.btn{display:flex;align-items:center;justify-content:center;background:var(--blue);color:var(--white);font-size:15px;font-weight:500;border-radius:2px;text-decoration:none}
.btn-inquiry{position:absolute;left:968px;top:24px;width:143px;height:34px}

/* hero */
.hero-copy{left:88px;top:220px;width:460px;color:var(--white)}
.hero-copy h1{font-size:37px;font-weight:500;line-height:1.2;margin-bottom:12px}
.hero-copy p{font-size:16.5px;line-height:1.4}
.btn-hero{position:absolute;left:89px;top:367px;width:126px;height:36px}
.dots{left:573px;top:481px;display:flex;gap:8px}
.dots span{width:13px;height:13px;border-radius:50%;border:1.5px solid #b8c6d6}
.dots span.on{border-color:var(--blue);background:radial-gradient(circle,var(--blue) 40%,transparent 45%)}

/* intro */
.intro-title{left:88px;top:614px;width:520px;font-size:26.5px;line-height:37px;font-weight:600;color:var(--blue)}
.intro-text{left:88px;top:748px;width:480px;font-size:15px;line-height:22px;color:var(--ink)}
.btn-outline{position:absolute;left:89px;top:849px;width:128px;height:36px;border:1.5px solid var(--blue);color:var(--blue);font-size:15px;display:flex;align-items:center;justify-content:center;border-radius:2px;text-decoration:none}

/* service tiles */
.tile-label{position:absolute;height:136px;background:var(--blue);color:var(--white);font-size:21px;font-weight:500;line-height:27px;display:flex;align-items:center;padding:0 22px 0 24px;white-space:nowrap;box-shadow:-6px 6px 16px rgba(0,0,0,.28)}

/* feature circles */
.feature{position:absolute;width:242px;text-align:center;color:var(--ink)}
.feature h3{font-size:18px;font-weight:500;margin:8px 0 6px}
.feature p{font-size:13px;line-height:18.5px;padding:0 24px}
.feature svg{display:block;margin:0 auto}

/* expertise */
.expertise{left:575px;top:1845px;width:520px;font-size:18.5px;line-height:25.6px;color:var(--ink)}
.expertise p+p{margin-top:25px}

/* cards */
.card{position:absolute;top:2338px;width:324px;height:271px;border-radius:16px;background:var(--white);overflow:hidden}
.card .photo{height:172px}
.card .card-body{position:absolute;left:24px;right:24px;top:172px;bottom:0;display:flex;align-items:center;justify-content:space-between}
.card h4{font-size:18px;font-weight:600;line-height:22px;color:var(--ink)}
.card .go{width:35px;height:35px;border-radius:50%;background:var(--slate);display:flex;align-items:center;justify-content:center}
.card.featured{background:var(--blue)}
.card.featured h4{color:var(--white)}
.card.featured .go{background:var(--white)}

/* inquiry */
.inquiry-title{left:0;top:2802px;width:1200px;text-align:center;font-size:33px;font-weight:600;color:var(--blue)}
.field{position:absolute;height:39px;border:1px solid var(--line);border-radius:3px;background:var(--white);display:flex;align-items:center;gap:9px;padding-left:10px;font-size:12.5px;color:var(--muted)}
.field.area{align-items:flex-start;padding-top:10px;height:107px}
.btn-submit{position:absolute;left:538px;top:3081px;width:126px;height:36px}

/* footer */
.footer-brand{left:88px;top:3340px;display:flex;align-items:center;gap:12px;font-size:30px;color:var(--white)}
.footer-brand .brand-dot{width:40px;height:40px}
.footer-col{position:absolute;top:3288px;color:var(--white)}
.footer-col h5{font-size:18px;font-weight:500;color:var(--blue);margin-bottom:16px}
.footer-col li{list-style:none;font-size:15px;line-height:31.3px}
.contact-row{display:flex;gap:13px;font-size:15px;line-height:20px;margin-bottom:11px}
.contact-row svg{flex:none;margin-top:2px}
.bottom-bar{left:0;top:3535px;width:1200px;height:43px;background:var(--blue-deep);color:var(--white);font-size:14px}
.bottom-bar .copy{position:absolute;left:88px;top:12px}
.social{position:absolute;right:88px;top:16px;display:flex;gap:21px}
.social span{width:11px;height:11px;border-radius:50%;background:var(--white)}
</style>
</head>
<body>
<div class="page">

<svg class="backdrop" width="1200" height="3578" viewBox="0 0 1200 3578">
  <defs>
    <linearGradient id="heroTone" x1="0" y1="0" x2="1" y2="1">
      <stop offset="0" stop-color="#505660"/>
      <stop offset=".45" stop-color="#2c313b"/>
      <stop offset="1" stop-color="#3a3f55"/>
    </linearGradient>
    <linearGradient id="footTone" x1="0" y1="0" x2="1" y2="1">
      <stop offset="0" stop-color="#3b4148"/>
      <stop offset=".5" stop-color="#23282e"/>
      <stop offset="1" stop-color="#30353c"/>
    </linearGradient>
    <linearGradient id="labTone" x1="0" y1="0" x2="1" y2="1">
      <stop offset="0" stop-color="#dfe4ea"/><stop offset=".6" stop-color="#9aa6b4"/><stop offset="1" stop-color="#c9d0d8"/>
    </linearGradient>
    <linearGradient id="stampTone" x1="0" y1="0" x2="1" y2="1">
      <stop offset="0" stop-color="#cfcac3"/><stop offset=".5" stop-color="#9a8f84"/><stop offset="1" stop-color="#e6e4e1"/>
    </linearGradient>
    <linearGradient id="benchTone" x1="0" y1="0" x2="1" y2="1">
      <stop offset="0" stop-color="#5d6168"/><stop offset=".5" stop-color="#b9bdc3"/><stop offset="1" stop-color="#e7e9ec"/>
    </linearGradient>
  </defs>

  <rect role="img" aria-label="Photo of sterilization equipment in a production room" x="0" y="72" width="1200" height="600" fill="url(#heroTone)"/>
  <path d="M0,72 L1200,72 L1200,90 C900,98 500,98 0,72Z" fill="#fff"/>

  <path d="M0,556 C260,528 560,520 780,545 C940,565 1080,600 1200,632 L1200,990 L0,990Z" fill="#fff"/>
  <path d="M0,506 C300,486 620,498 860,548 C700,528 360,528 0,556Z" fill="var(--blue)"/>

  <rect x="0" y="979" width="1200" height="760" fill="var(--slate)"/>
  <path d="M1000,1045 L1200,997 L1200,979 L980,979Z" fill="#fff"/>
  <path d="M0,979 L945,979 C990,981 1000,1020 982,1048 L840,1246 C810,1288 782,1299 740,1299 L0,1299Z" fill="var(--blue)"/>

  <polygon role="img" aria-label="Photo of a sterilization chamber door" points="97,1028 354,1028 386,1257 129,1257" fill="url(#labTone)"/>
  <polygon role="img" aria-label="Photo of an assembly and packaging bench" points="450,1028 706,1028 736,1257 482,1257" fill="url(#labTone)"/>

  <circle cx="293" cy="1486" r="121" fill="#fff"/>
  <circle cx="599" cy="1486" r="121" fill="#fff"/>
  <circle cx="906" cy="1486" r="128" fill="none" stroke="var(--blue)" stroke-width="8"/>
  <circle cx="906" cy="1486" r="119" fill="#fff"/>

  <path d="M0,1775 C300,1705 560,1672 800,1674 C1000,1676 1120,1710 1200,1778 L1200,2125 C900,2240 500,2250 0,2098Z" fill="#fff"/>
  <path d="M420,1690 C700,1660 1020,1662 1200,1681 L1200,1778 C1120,1710 1000,1676 800,1674 C650,1673 520,1680 420,1690Z" fill="var(--blue)"/>
  <path d="M0,2098 C220,2175 420,2222 560,2236 C380,2232 180,2198 0,2158Z" fill="var(--blue)"/>

  <circle cx="324" cy="1963" r="180" fill="none" stroke="var(--blue)" stroke-width="5"/>
  <circle role="img" aria-label="Photo of a gloved hand loading test vials into a sterilization rack" cx="324" cy="1963" r="172" fill="url(#benchTone)"/>

  <circle cx="927" cy="718" r="180" fill="none" stroke="var(--blue)" stroke-width="5"/>
  <circle role="img" aria-label="Photo of a hand pressing a rubber stamp on a document" cx="927" cy="718" r="172" fill="url(#stampTone)"/>

  <path d="M0,2813 C300,2740 700,2700 1200,2708 L1200,3146 C900,3230 500,3230 0,3084Z" fill="#fff"/>
  <path d="M500,2718 C750,2698 1000,2700 1200,2722 L1200,2820 C1050,2760 800,2720 500,2718Z" fill="var(--blue)"/>
  <path d="M0,3084 C200,3160 420,3205 600,3212 C380,3218 180,3190 0,3140Z" fill="var(--blue)"/>
  <path d="M800,3196 C960,3185 1100,3165 1200,3146 L1200,3200 C1080,3210 940,3210 800,3196Z" fill="var(--blue)"/>

  <path role="img" aria-label="Blurred photo of a production floor" d="M0,3140 C180,3190 380,3218 600,3212 C860,3208 1060,3200 1200,3200 L1200,3535 L0,3535Z" fill="url(#footTone)"/>
</svg>

<header class="site-header">
  <div class="brand"><span class="brand-dot"></span>TallowPine</div>
  <nav class="main-nav">
    <a class="active" href="#">Home</a><a href="#">Services</a><a href="#">About Us</a><a href="#">Support</a>
  </nav>
  <a class="btn btn-inquiry" href="#">Quick Inquiry</a>
</header>

<section class="abs hero-copy">
  <h1>Sterilization Solutions</h1>
  <p>Tallow Pine is committed to finding the most suitable and efficient sterilization method for our customers' products.</p>
</section>
<a class="btn btn-hero" href="#">Contact Us</a>
<div class="abs dots"><span></span><span class="on"></span><span></span></div>

<h2 class="abs intro-title">Allow us to help you navigate every<br>regulatory hurdle that comes with<br>bringing your product to market</h2>
<p class="abs intro-text">Tallow Pine is committed to providing our customers with continued assurance of compliance with today's evolving regulatory requirements.</p>
<a class="btn-outline" href="#">Contact Us</a>

<div class="tile-label" style="left:285px;top:1092px">Sterilization<br>Solutions</div>
<div class="tile-label" style="left:639px;top:1092px">Quality Assembly<br>&amp; Packaging</div>

<div class="feature" style="left:172px;top:1400px">
  <svg width="46" height="46" viewBox="0 0 46 46" fill="none" stroke="var(--blue)" stroke-width="3"><path d="M23 33C15 24 12 19 12 14a11 11 0 0 1 22 0c0 5-3 10-11 19Z"/><circle cx="23" cy="14" r="4"/><path d="M13 34c-4 1-6 3-6 4 0 3 7 5 16 5s16-2 16-5c0-1-2-3-6-4"/></svg>
  <h3>Our Location</h3>
  <p>Tallow Pine is located on the beautiful Central Coast of California mid-way...</p>
</div>
<div class="feature" style="left:478px;top:1400px">
  <svg width="46" height="46" viewBox="0 0 46 46" fill="none" stroke="var(--blue)" stroke-width="3"><path d="M6 44V8h12v36M18 44V22h14v22M4 44h30"/><path d="M10 14h4M10 22h4M10 30h4M23 30h4M23 37h4"/><circle cx="36" cy="10" r="4"/><path d="M36 2v3M36 15v3M28 10h3M41 10h3"/></svg>
  <h3>Our Facility</h3>
  <p>Our modern 20,000 square foot facility was designed to exceed today's regulatory requirements...</p>
</div>
<div class="feature" style="left:785px;top:1410px">
  <svg width="46" height="46" viewBox="0 0 46 46" fill="none" stroke="var(--blue)" stroke-width="3"><circle cx="23" cy="23" r="19"/><path d="M17 22a6 6 0 1 1 12 0c0 3-3 4-3 7h-6c0-3-3-4-3-7Z"/><path d="M20 33h6"/></svg>
  <h3>Our Expertise</h3>
  <p>Tallow Pine's areas of expertise include manufacturing and packaging...</p>
</div>

<section class="abs expertise">
  <p>Tallow Pine offers deep and vast knowledge in the realm of sterilization and, in particular, detailed guidance with our vertically integrated Hydrogen Peroxide Gas Plasma sterilization modality.</p>
  <p>Assistance with the development and comparisons of full validation and batch release can be provided to OEMs to help you select the best path forward for your project.</p>
</section>

<article class="card" style="left:88px">
  <div class="photo" role="img" aria-label="Photo of warehouse staff packing boxes" style="background:linear-gradient(135deg,#6b5a4b,#b79a7e 55%,#3f4652)"></div>
  <div class="card-body"><h4>Contract Assembly &amp;<br>Packaging</h4><span class="go"><svg width="14" height="14" viewBox="0 0 14 14" fill="none" stroke="#fff" stroke-width="2"><path d="M1 7h11M7 2l5 5-5 5"/></svg></span></div>
</article>
<article class="card" style="left:438px">
  <div class="photo" role="img" aria-label="Illustration of digital support service icons" style="background:linear-gradient(135deg,#0d2f45,#1b8ab5 55%,#0a1f30)"></div>
  <div class="card-body"><h4>Support Services</h4><span class="go"><svg width="14" height="14" viewBox="0 0 14 14" fill="none" stroke="#fff" stroke-width="2"><path d="M1 7h11M7 2l5 5-5 5"/></svg></span></div>
</article>
<article class="card featured" style="left:788px">
  <div class="photo" role="img" aria-label="Photo of a worker checking stock on a tablet" style="background:linear-gradient(135deg,#2b3340,#a88a6a 60%,#d8c4ae)"></div>
  <div class="card-body"><h4>Inventory Control</h4><span class="go"><svg width="14" height="14" viewBox="0 0 14 14" fill="none" stroke="var(--blue)" stroke-width="2"><path d="M1 7h11M7 2l5 5-5 5"/></svg></span></div>
</article>

<h2 class="abs inquiry-title">Quick Inquiry</h2>
<div class="field" style="left:125px;top:2878px;width:307px"><svg width="14" height="14" viewBox="0 0 14 14" fill="none" stroke="var(--blue)" stroke-width="1.4"><circle cx="7" cy="4.5" r="3"/><path d="M1.5 13c0-3 2.5-5 5.5-5s5.5 2 5.5 5Z"/></svg>Name</div>
<div class="field" style="left:446px;top:2878px;width:307px"><svg width="14" height="14" viewBox="0 0 14 14" fill="none" stroke="var(--blue)" stroke-width="1.4"><rect x="1" y="3" width="12" height="9"/><path d="M1 3l6 5 6-5"/></svg>Email</div>
<div class="field" style="left:768px;top:2878px;width:307px"><svg width="14" height="14" viewBox="0 0 14 14" fill="none" stroke="var(--blue)" stroke-width="1.4"><rect x="3.5" y="1" width="7" height="12" rx="1"/><path d="M6 11h2"/></svg>Phone</div>
<div class="field area" style="left:125px;top:2932px;width:950px"><svg width="14" height="14" viewBox="0 0 14 14" fill="none" stroke="var(--blue)" stroke-width="1.4"><path d="M1.5 1.5h11v7l-4 4h-7Z"/><path d="M8.5 12.5v-4h4"/></svg>How can we help?</div>
<a class="btn btn-submit" href="#">Submit</a>

<div class="abs footer-brand"><span class="brand-dot"></span>TallowPine</div>
<div class="footer-col" style="left:351px">
  <h5>Quick Link</h5>
  <ul><li>Sterilization</li><li>Packaging</li><li>Contract Manufacturing</li><li>New Product Introduction</li><li>Validations</li></ul>
</div>
<div class="footer-col" style="left:615px">
  <h5>Company</h5>
  <ul><li>About Us</li><li>Careers</li><li>Contact Us</li><li>Network</li></ul>
</div>
<div class="footer-col" style="left:879px">
  <h5>Contact Info</h5>
  <div class="contact-row" style="margin-top:8px"><svg width="16" height="18" viewBox="0 0 16 18" fill="none" stroke="var(--blue)" stroke-width="2"><path d="M8 17C3 11 1.5 8.5 1.5 6a6.5 6.5 0 0 1 13 0c0 2.5-1.5 5-6.5 11Z"/><circle cx="8" cy="6" r="2"/></svg><span>418 Cedar Hollow Rd,<br>Marlow Springs, CA 93512</span></div>
  <div class="contact-row"><svg width="16" height="16" viewBox="0 0 16 16" fill="var(--blue)"><path d="M3 1l3 3-2 2c1 2 3 4 6 6l2-2 3 3-2 2C7 15 1 9 1 3Z"/></svg><span>(555) 014-2290</span></div>
  <div class="contact-row"><svg width="16" height="16" viewBox="0 0 16 16" fill="var(--blue)"><rect x="4" y="1" width="8" height="5"/><rect x="1" y="6" width="14" height="7" rx="1"/><rect x="4" y="10" width="8" height="5" fill="#fff"/></svg><span>(555) 014-2291</span></div>
  <div class="contact-row"><svg width="16" height="16" viewBox="0 0 16 16" fill="var(--blue)"><path d="M1 3h14v10H1Z"/><path d="M1 3l7 6 7-6" fill="none" stroke="#fff" stroke-width="1.3"/></svg><span>info@tallowpine.com</span></div>
</div>

<footer class="abs bottom-bar">
  <span class="copy">Copyright © 2021 TallowPine. All Rights Reserved</span>
  <div class="social"><span></span><span></span><span></span><span></span></div>
</footer>

</div>
</body>
</html>
```